GLS biz card

We need a business card design for our new company based in Los Angeles called "Gold Lantern Studios". We develop film and television projects. We work with investors, financiers, film production companies, film distribution and sales companies as well as studios. We would like to incorporate our logo (see attached) on a two-sided card. We need to include: name and title, address, phone, email and company website.

Target Market(s)

Business, financial and studio clients

Industry/Entity Type

Business

Contact Information for Business Card

Two-sided. We are thinking of the logo on one side and the information on the back. Please feel free to be creative! Thanks.

Requirements
Must have
• Please include the following text information, excluding the "CAPS CATEGORY:" and please allow the ability for us to change the name, title and email address for each company employee):
• NAME & TITLE:
• Peter Dunmore
• Managing Partner
• COMPANY NAME:
• GOLD LANTERN STUDIOS (please use existing logo)
• COMPANY ADDRESS:
• KVT Arts Park
• 2480 Wexley Boulevard
• Arts Hall, 4th Floor
• Harbor Point, CA 90412
• COMPANY PHONE NUMBER:
• 310-555-4206
• COMPANY WEBSITE ADDRESS:
• www.goldlanternstudioshouse.com
• EMAIL ADDRESS: (only one per card)
• frank@goldlanternstudioshouse.com
• tizzy@goldlanternstudioshouse.com
• peter@goldlanternstudioshouse.com

```html
<!DOCTYPE html>
<html lang="en">
<head>
<meta charset="utf-8">
<title>Gold Lantern Studios – Business Card</title>
<link href="https://fonts.googleapis.com/css2?family=Raleway:wght@300;600&family=Ubuntu:wght@400;500;700&display=swap" rel="stylesheet">
<style>
  :root {
    --page-bg: #e3e4e6;
    --card-bg: #050709;
    --card-bg-top: #0b0d11;
    --brand-blue: #1fa6de;
    --glow-blue: #3c8cff;
    --text-grey: #a7a9ad;
    --text-light: #c9cacc;
    --tagline-white: #f2f2f2;
  }
  * { box-sizing: border-box; margin: 0; padding: 0; }
  html, body {
    width: 1200px;
    height: 1200px;
    overflow: hidden;
    background: var(--page-bg);
  }
  .card {
    position: absolute;
    left: 173px;
    width: 853px;
    height: 488px;
    overflow: hidden;
  }
  .card--front {
    top: 69px;
    background: linear-gradient(180deg, var(--card-bg-top) 0%, var(--card-bg) 45%, #0d0f13 100%);
  }
  .card--back {
    top: 642px;
    height: 490px;
    background: var(--card-bg);
  }

  /* brand block */
  .brand-dot {
    position: absolute;
    border-radius: 50%;
    background: var(--brand-blue);
  }
  .brand-name {
    position: absolute;
    font-family: "Ubuntu", sans-serif;
    font-weight: 700;
    color: var(--brand-blue);
    white-space: nowrap;
    transform: translateX(-50%);
    text-align: center;
  }
  .card--front .brand-dot { left: 108px; top: 56px; width: 108px; height: 108px; }
  .card--front .brand-name { left: 161px; top: 196px; font-size: 17px; letter-spacing: 1.2px; }

  .card--back .brand-dot { left: 363px; top: 97px; width: 130px; height: 130px; }
  .card--back .brand-name { left: 427px; top: 276px; font-size: 32px; letter-spacing: 2px; }

  /* person */
  .person-name {
    position: absolute;
    left: 428px;
    top: 96px;
    font-family: "Raleway", sans-serif;
    font-weight: 300;
    font-size: 40px;
    color: var(--text-light);
  }
  .person-title {
    position: absolute;
    left: 428px;
    top: 148px;
    font-family: "Raleway", sans-serif;
    font-weight: 600;
    font-size: 23px;
    color: var(--text-grey);
  }

  /* light streak */
  .light-glow {
    position: absolute;
    left: 0; right: 0;
    top: 236px;
    height: 100px;
    background: radial-gradient(ellipse 60% 50% at 50% 50%, rgba(40, 110, 230, 0.35), rgba(20, 60, 140, 0.12) 55%, transparent 80%);
  }
  .light-line {
    position: absolute;
    left: 0; right: 0;
    top: 285px;
    height: 2px;
    background: linear-gradient(90deg, rgba(60,140,255,0.35), var(--glow-blue) 35%, #e6f3ff 50%, var(--glow-blue) 65%, rgba(60,140,255,0.35));
    box-shadow: 0 0 10px 2px rgba(60, 140, 255, 0.6);
  }

  /* contact block */
  .contact {
    position: absolute;
    left: 0; right: 0;
    top: 357px;
    font-family: "Ubuntu", sans-serif;
    font-style: normal;
    font-weight: 400;
    font-size: 21px;
    line-height: 27px;
    color: var(--text-grey);
    text-align: center;
    white-space: nowrap;
  }
  .sep { margin: 0 6px; }

  /* back details */
  .tagline {
    position: absolute;
    left: 0; right: 0;
    top: 342px;
    text-align: center;
    font-family: "Ubuntu", sans-serif;
    font-weight: 700;
    font-size: 12px;
    letter-spacing: 3.4px;
    color: var(--tagline-white);
  }
  .website {
    position: absolute;
    left: 0; right: 0;
    top: 424px;
    text-align: center;
    font-family: "Ubuntu", sans-serif;
    font-weight: 400;
    font-size: 22px;
    color: var(--text-grey);
  }
</style>
</head>
<body>
  <section class="card card--front">
    <div class="brand-dot"></div>
    <div class="brand-name">GOLD LANTERN STUDIOS</div>

    <h1 class="person-name">Peter Dunmore</h1>
    <p class="person-title">President <span class="sep">||</span> CEO</p>

    <div class="light-glow"></div>
    <div class="light-line"></div>

    <address class="contact">
      <div>KVT Arts Park <span class="sep">||</span> 2480 Wexley Boulevard</div>
      <div>Arts Hall, 4th Floor <span class="sep">||</span> Harbor Point, CA 90412</div>
      <div>310-555-4206 <span class="sep">||</span> peter@goldlanternstudioshouse.com</div>
    </address>
  </section>

  <section class="card card--back">
    <div class="brand-dot"></div>
    <div class="brand-name">GOLD LANTERN STUDIOS</div>
    <p class="tagline">A MEDIA ENTERTAINMENT COMPANY</p>
    <p class="website">www.goldlanternstudioshouse.com</p>
  </section>
</body>
</html>
```